Blue Ride Business Cards

**As soon as there are some quality ideas presented, I will guarantee payment**

We require a template business card with 3 variations based on the following roles:

**Driver Specific version
Communicate;

-More customers, tips, safety, money
-GPS enabled
-no commitment required
-WE PAY YOU (first 3 months)
-Signup here: www.blueride.ca/drivers
-Incorporate QR code - provided
-Customer ratings
-Brokerage independent

**Staff Specific version
Communicate;

-www.blueride.ca
-GPS enabled hailing solution
-Taxis, Limosines, Town Cars
-Name, phone, email

**Customer Specific version
Communicate;
-www.blueride.ca
-Free Service
-Driver ratings
-No busy signals

Logo - provided
Main colours - Black, Yellow
Double sided card
Updates

Thanks for all the submissions, as promised, now that there are some sufficiently creative submissions I have guaranteed this project.  I will be giving some feedback and additional direction today.

Thanks,
Marlon

A couple additional requirements;

The "customer" card will require 2 QR codes on it.  1 for iPhone app install and the other for Android app install.

All QR codes need to be at least 3.2cm x 3.2cm

Reason: Reason for extension is that I've gotten busy with another aspect of my business and haven't been able to provide feedback in a timely manner. Hence none of the designs are currently developed to the point that I'm ready to close the contest. PLEASE re-read the design brief to ensure you are addressing the requirements!

Industry/Entity Type

Business

Requirements
Must have
• The full logo on at least one side of the card. Just "BlueRide" text on the other is fine.

QR code integrated into card design

Clean and Simple design with high contrast
Should not have
• cluttered or overly ornate / fancy text

```html
<!DOCTYPE html>
<html lang="en">
<head>
<meta charset="utf-8">
<title>Blue Ride Business Card</title>
<link rel="stylesheet" href="https://fonts.googleapis.com/css2?family=Montserrat:wght@800&display=swap">
<style>
  :root {
    --card-black: #000000;
    --taxi-yellow: #f5e50f;
    --taxi-yellow-glow: rgba(245, 229, 15, 0.55);
    --brand-white: #ffffff;
  }
  html, body {
    margin: 0;
    padding: 0;
    width: 1200px;
    height: 680px;
    overflow: hidden;
    background: var(--card-black);
  }
  .business-card {
    position: relative;
    width: 1200px;
    height: 680px;
    background: var(--card-black);
    overflow: hidden;
  }
  .brand-name {
    position: absolute;
    left: 0;
    right: 0;
    top: 228px;
    margin: 0;
    text-align: center;
    font-family: "Montserrat", sans-serif;
    font-weight: 800;
    font-size: 124px;
    line-height: 1;
    letter-spacing: -2px;
    color: var(--brand-white);
  }
  .taxi-band {
    position: absolute;
    left: 0;
    top: 466px;
    width: 1200px;
    height: 184px;
    background: linear-gradient(180deg,
      var(--taxi-yellow-glow) 0%,
      var(--taxi-yellow) 30%,
      var(--taxi-yellow) 70%,
      var(--taxi-yellow-glow) 100%);
    box-shadow: 0 0 40px var(--taxi-yellow-glow);
  }
</style>
</head>
<body>
  <main class="business-card">
    <h1 class="brand-name">BlueRide</h1>
    <div class="taxi-band" role="img" aria-label="Glowing yellow taxi checker band across the lower edge of the card"></div>
  </main>
</body>
</html>
```